Corvath Properties Business Card Design

We would now like to design business cards with the new Corvath Properties logo

Target Market(s)

Professional

Industry/Entity Type

Professional services

Contact Information for Business Card

Employee name, title, phone number, email address, corporate office address and logo.

Font styles to use
Sans Serif

Colors
0054AA
0677BA
7BADD7
CADEEF
E8F1F8

Requirements
Must have
• My logo
Should not have
• any other pictures or images besides my logo

```html
<!DOCTYPE html>
<html lang="en">
<head>
<meta charset="utf-8">
<title>Corvath Properties Business Card</title>
<link href="https://fonts.googleapis.com/css2?family=Open+Sans:wght@400;600;700&display=swap" rel="stylesheet">
<style>
  :root {
    --backdrop: #3b3b3b;
    --card: #1a1a1b;
    --brand-blue: #3a86d6;
    --deep-blue: #0054aa;
    --text-light: #e6e6e6;
    --pattern-dark: #141415;
    --pattern-mid: #2a2a2c;
  }
  * { margin: 0; padding: 0; box-sizing: border-box; }
  html, body {
    width: 1200px; height: 801px; overflow: hidden;
    background: var(--backdrop);
    font-family: "Open Sans", Arial, sans-serif;
  }
  .stage {
    position: relative; width: 1200px; height: 801px;
    display: flex; align-items: center; justify-content: center; gap: 50px;
  }
  .card {
    position: relative; width: 525px; height: 300px;
    background: var(--card);
    border-bottom: 3px solid var(--brand-blue);
    border-left: 2px solid var(--brand-blue);
    box-shadow: 0 10px 30px rgba(0,0,0,.45);
    overflow: hidden;
  }
  /* Front */
  .brand {
    position: absolute; left: 32px; top: 58px;
    display: flex; align-items: center; gap: 12px;
  }
  .brand-square { width: 34px; height: 34px; background: var(--brand-blue); flex: none; }
  .brand-name {
    color: var(--brand-blue); font-weight: 700; font-size: 21px;
    line-height: 1.15; letter-spacing: .5px; text-transform: uppercase;
  }
  .identity {
    position: absolute; right: 32px; top: 54px; text-align: right;
  }
  .person-name {
    color: var(--brand-blue); font-weight: 700; font-size: 20px;
    letter-spacing: .5px; text-transform: uppercase;
  }
  .person-title { color: var(--text-light); font-size: 12px; margin-top: 2px; }
  .divider {
    position: absolute; left: 32px; right: 32px; top: 160px;
    height: 1px; background: var(--brand-blue);
  }
  .contacts {
    position: absolute; left: 32px; top: 190px; list-style: none;
    color: var(--text-light); font-size: 13px; line-height: 1.55;
  }
  .contacts li { display: flex; align-items: center; gap: 8px; }
  .contacts svg { width: 11px; height: 11px; flex: none; }
  .icon-fill { fill: var(--brand-blue); }
  .icon-line { fill: none; stroke: var(--brand-blue); stroke-width: 2.5; }
  .address {
    position: absolute; right: 32px; top: 190px; text-align: right;
    color: var(--text-light); font-size: 13px; line-height: 1.55; font-style: normal;
  }
  /* Back */
  .pattern {
    position: absolute; inset: 0;
    background: linear-gradient(120deg, var(--pattern-dark) 0%, var(--pattern-mid) 55%, var(--pattern-dark) 100%);
  }
  .back-brand {
    position: absolute; right: 40px; bottom: 40px;
    display: flex; align-items: center; gap: 10px;
  }
</style>
</head>
<body>
<main class="stage">
  <section class="card card-front">
    <div class="brand">
      <span class="brand-square"></span>
      <span class="brand-name">Corvath<br>Properties</span>
    </div>
    <div class="identity">
      <p class="person-name">Dalen Marsh</p>
      <p class="person-title">CEO</p>
    </div>
    <div class="divider"></div>
    <ul class="contacts">
      <li><svg viewBox="0 0 24 24"><path class="icon-fill" d="M6.6 10.8a15 15 0 0 0 6.6 6.6l2.2-2.2c.3-.3.7-.4 1-.2 1.1.4 2.3.6 3.6.6.6 0 1 .4 1 1V20c0 .6-.4 1-1 1A17 17 0 0 1 3 4c0-.6.4-1 1-1h3.5c.6 0 1 .4 1 1 0 1.3.2 2.5.6 3.6.1.3 0 .7-.2 1z"/></svg>555-018-4427</li>
      <li><svg viewBox="0 0 24 24"><path class="icon-line" d="M3 6h18v12H3z M3 6l9 7 9-7"/></svg>dmarsh@corvathprop.com</li>
      <li><svg viewBox="0 0 24 24"><circle class="icon-fill" cx="12" cy="12" r="10"/></svg>www.corvathprop.com</li>
    </ul>
    <address class="address">418 Alder Brook Road<br>Westfield, CT 062</address>
  </section>

  <section class="card card-back">
    <div class="pattern" role="img" aria-label="Embossed repeating monogram pattern in dark tones"></div>
    <div class="back-brand">
      <span class="brand-square"></span>
      <span class="brand-name">Corvath<br>Properties</span>
    </div>
  </section>
</main>
</body>
</html>
```